Managed Service Provider need new business cards

We are a small Maanged Service Provider of IT Services and need a new fresh design for our business cards. We want something impossible, fun and professional :)
Our services has a large range, but we are always fun and make sure our customers both get their issue sorted and also feel like they are "catching up with an old friend".
All our cards in the past has always been all black, with red and we need something fresher.
The back of card, we would like just a small list of what we do i think, but if someone has a better idea, please do something cool with the back of the card:
Managed IT Services
Productivity Solutions
Data Backup and Recovery
IT System Maintenance
Managed IT Security
More details can be found on our website tqnetworks.com.au
Industry/Entity Type
It Company
Contact Information for Business Card
Name: Dwayne Falstrup
Title: Director
Phone: 03 6193 4827
Mobile: 0412 587 239
Email: dwayne@tqnetworks.com.au
Web: www.tqnetworks.com.au

```html
<!DOCTYPE html>
<html lang="en">
<head>
<meta charset="utf-8">
<title>TQ Networks – Business Cards</title>
<link rel="stylesheet" href="https://fonts.googleapis.com/css2?family=Poppins:wght@400;500;600&display=swap">
<style>
  :root {
    --page-bg: #f0f0f0;
    --card-dark: #3a3a3a;
    --card-light: #f7f7f7;
    --brand-red: #e3151b;
    --ink: #2e2e2e;
    --ink-soft: #6a6a6a;
    --white: #ffffff;
  }
  * { margin: 0; padding: 0; box-sizing: border-box; }
  html, body {
    width: 1200px; height: 1200px; overflow: hidden;
    background: var(--page-bg);
    font-family: "Poppins", sans-serif;
  }
  .canvas { position: relative; width: 1200px; height: 1200px; }

  .card { position: absolute; overflow: hidden; }

  /* Front */
  .card-front {
    left: 208px; top: 109px; width: 767px; height: 447px;
    background: var(--card-dark);
  }
  .front-wordmark {
    position: absolute; left: 0; right: 0; top: 250px;
    transform: translateY(-50%);
    text-align: center;
    font-size: 58px; font-weight: 600; letter-spacing: 1px;
    color: var(--brand-red);
  }
  .front-url {
    position: absolute; left: 0; right: 0; bottom: 20px;
    text-align: center;
    font-size: 11px; letter-spacing: 14px;
    color: var(--white);
  }

  /* Back */
  .card-back {
    left: 208px; top: 620px; width: 769px; height: 446px;
    background: var(--card-dark);
  }
  .back-info {
    position: absolute; left: 0; top: 0; width: 100%; height: 223px;
    background: var(--card-light);
  }
  .person-name {
    position: absolute; left: 51px; top: 34px;
    font-size: 20px; font-weight: 600; letter-spacing: 1px;
    color: var(--ink); text-transform: uppercase;
  }
  .person-name .surname { color: var(--brand-red); }
  .person-title {
    position: absolute; left: 52px; top: 62px;
    font-size: 10.5px; color: var(--ink-soft);
  }
  .contact-list {
    position: absolute; left: 52px; top: 104px; list-style: none;
  }
  .contact-list li {
    font-size: 11px; color: var(--ink-soft); height: 23px; line-height: 23px;
  }
  .contact-list li.phone { font-size: 14px; }
  .contact-label {
    display: inline-block; width: 14px;
    font-size: 10px; font-weight: 600; color: var(--brand-red);
  }
  .back-wordmark {
    position: absolute; right: 40px; top: 86px;
    font-size: 38px; font-weight: 600; letter-spacing: 0.5px;
    color: var(--brand-red);
  }
  .services {
    position: absolute; left: 0; right: 0; top: 285px;
    text-align: center; color: var(--white);
  }
  .services-heading {
    font-size: 12px; font-weight: 600; letter-spacing: 2px; margin-bottom: 20px;
  }
  .services-heading .accent { color: var(--brand-red); }
  .services-list {
    font-size: 15px; letter-spacing: 1.6px; line-height: 28px;
  }
</style>
</head>
<body>
<main class="canvas">

  <section class="card card-front" aria-label="Card front">
    <div class="front-wordmark">TQ Networks</div>
    <div class="front-url">www.tqnetworks.com.au</div>
  </section>

  <section class="card card-back" aria-label="Card back">
    <div class="back-info">
      <h1 class="person-name">Dwayne <span class="surname">Falstrup</span></h1>
      <p class="person-title">Managing Director</p>
      <ul class="contact-list">
        <li class="phone"><span class="contact-label">T</span>: 03 6193 4827 &nbsp;, 0412 587 239</li>
        <li><span class="contact-label">E</span>: dwayne@tqnetworks.com.au</li>
        <li><span class="contact-label">W</span>: www.tqnetworks.com.au</li>
      </ul>
      <div class="back-wordmark">TQ Networks</div>
    </div>

    <div class="services">
      <h2 class="services-heading">Our <span class="accent">Services</span></h2>
      <p class="services-list">-Managed IT Services &nbsp;– Productivity Solutions – Data Backup and Recovery<br>– IT System Maintenance – Managed IT Security</p>
    </div>
  </section>

</main>
</body>
</html>
```